Online trading school - Website design

We are building an online trading school (trading of shares, commodities, indices, currencies). The purpose is to teach online traders how to trade successfully. We need to design the homepage of the website and logo (bramwelloq.com will be the domain). The homepage will contain the following elements

- logo
- Sign in and Register links/buttons
- upper menu
- short introduction
- a couple of bullet points 'Why to join our school?'
- sign up form
- text
- bottom menu

Attached is a draft for the designer. The draft is just for an inspiration, the actual structure of the website can be different if the designer thinks so.

The designer is free to choose colors.

School

3 page

```html
<!DOCTYPE html>
<html lang="en">
<head>
<meta charset="utf-8">
<title>Bramwelloq — Online Trading School</title>
<link rel="stylesheet" href="https://fonts.googleapis.com/css2?family=Open+Sans:wght@400;600;700;800&display=swap">
<style>
:root{
  --ink:#111317;
  --header:#161719;
  --nav:#1d232c;
  --blue:#1565c8;
  --blue-dark:#0f4fa3;
  --green:#17a633;
  --text:#5b5f66;
  --muted:#8c9097;
  --line:#e3e6ea;
  --soft:#eeeff1;
  --footer:#232a35;
  --footer-deep:#1b2029;
  --white:#ffffff;
}
*{box-sizing:border-box;margin:0;padding:0}
html,body{width:1200px;height:3103px;overflow:hidden;background:var(--white)}
body{font-family:"Open Sans",Arial,sans-serif;color:var(--text);position:relative}
.page{position:relative;width:1200px;height:3103px;overflow:hidden}
.abs{position:absolute}
a{color:inherit;text-decoration:none}

/* top bar */
.topbar{left:0;top:0;width:1200px;height:35px;background:var(--ink);color:#d8d8d8;font-size:11px;font-weight:600}
.topbar .call{position:absolute;left:242px;top:10px}
.topbar .follow{position:absolute;left:793px;top:10px}
.social{position:absolute;top:4px;display:flex;gap:6px}
.social span{width:27px;height:27px;border:1px solid #3a3d42;display:block}
.social span::after{content:"";display:block;width:7px;height:7px;background:#cfd2d6;margin:9px auto 0;border-radius:50%}
.topbar .social{left:855px}

/* header */
.header{left:0;top:35px;width:1200px;height:93px;background:var(--header)}
.logo{position:absolute;display:flex;align-items:center;gap:8px;border:3px solid #fff;padding:2px 12px;font-weight:800;color:#fff}
.header .logo{left:242px;top:23px;height:58px;font-size:34px;letter-spacing:-.5px;width:226px;justify-content:center}
.btn-signin{left:668px;top:35px;width:139px;height:44px;border:1px solid #9aa0a8;color:#fff;font-size:11px;font-weight:700;display:flex;align-items:center;justify-content:center;gap:8px}
.btn-register{left:815px;top:35px;width:139px;height:44px;background:var(--green);color:#fff;font-size:11px;font-weight:700;display:flex;align-items:center;justify-content:center;gap:8px}

/* nav */
.nav{left:0;top:128px;width:1200px;height:48px;background:var(--nav)}
.nav ul{list-style:none;display:flex;position:absolute;left:242px;top:16px;font-size:11px;font-weight:700;color:#fff;letter-spacing:.3px}
.nav li+li::before{content:"/";margin:0 14px;color:#8d949e}

/* hero */
.hero{left:0;top:176px;width:1200px;height:501px;background:linear-gradient(100deg,#2d3a4c 0%,#4a5668 35%,#6f7a88 60%,#9aa3ad 100%)}
.hero h1{position:absolute;left:242px;top:128px;width:420px;color:#fff;font-size:31px;line-height:37px;font-weight:700;letter-spacing:.5px}
.hero p{position:absolute;left:242px;top:224px;width:410px;color:#eef1f5;font-size:12.5px;line-height:19px}
.slide-arrow{position:absolute;top:232px;width:46px;height:39px;background:var(--blue);display:flex;align-items:center;justify-content:center}

/* split button */
.split-btn{position:absolute;display:flex;border:1px solid var(--blue);background:#fff}
.split-btn .label{background:var(--blue);color:#fff;font-size:11px;font-weight:700;display:flex;align-items:center;padding-left:28px;clip-path:polygon(0 0,100% 0,82% 100%,0 100%)}
.split-btn .go{flex:1;display:flex;align-items:center;justify-content:center}

/* features */
.feature{position:absolute;top:724px;width:230px;display:flex;gap:12px}
.feature h3{font-size:10.5px;font-weight:700;color:#23272d;margin:10px 0 6px}
.feature p{font-size:10.5px;line-height:15px;color:var(--muted)}
.divider{left:242px;top:872px;width:716px;height:1px;background:var(--line)}

/* why join */
.section-title{color:var(--blue);font-weight:600;font-size:30px}
.why-title{left:242px;top:924px}
.why-text{left:242px;top:983px;width:290px;font-size:10.5px;line-height:15px;color:var(--text)}
.ticks{left:242px;top:1060px;list-style:none}
.ticks li{display:flex;align-items:center;gap:16px;font-size:11.5px;color:#2d3137;height:26px}
.ticks li:nth-child(2){margin-top:17px}
.ticks li:nth-child(3){margin-top:24px}
.ticks li:nth-child(4){margin-top:24px}
.ticks li:nth-child(5){margin-top:24px}
.why-photo{left:608px;top:987px;width:348px;height:248px;box-shadow:0 4px 14px rgba(0,0,0,.25);background:linear-gradient(135deg,#49525e 0%,#9aa3ae 40%,#e4e7ea 65%,#7e8690 100%)}

/* join school */
.join{left:0;top:1463px;width:1200px;height:312px;background:linear-gradient(90deg,#59544a 0%,#7a7468 30%,#c9c7c4 55%,#eeeeee 70%,#efefef 100%)}
.join h2{position:absolute;left:242px;top:50px;color:#fff;font-size:37px;line-height:42px;font-weight:800;letter-spacing:.5px}
.join p{position:absolute;left:242px;top:152px;width:230px;color:#f2f2f2;font-size:10px;line-height:14px}
.field{position:absolute;left:730px;width:226px;height:30px;border:1px solid #c9dcf3;background:#fff;font-size:9px;color:#9aa0a8;padding:9px 0 0 8px}
.agree{position:absolute;left:730px;top:187px;display:flex;align-items:center;gap:10px;font-size:9px;color:#8a8f96}
.agree i{width:9px;height:9px;border:1px solid #b9bec5;display:block;background:#fff}

/* offer */
.offer-title{left:0;top:1860px;width:1200px;text-align:center}
.offer-text{left:279px;top:1924px;width:644px;text-align:center;font-size:10px;line-height:15px;color:var(--text)}
.cards{left:242px;top:2028px;width:716px;height:252px;display:flex;gap:2px}
.card{flex:1;position:relative;background:linear-gradient(160deg,#6d5a4d 0%,#b99d86 40%,#d8cbbb 70%,#8e8078 100%)}
.card:nth-child(2){background:linear-gradient(160deg,#3b3f45 0%,#9a9ea4 45%,#c9c5c0 100%)}
.card:nth-child(3){background:linear-gradient(160deg,#7a3630 0%,#b4574d 45%,#c7b9a8 100%)}
.card:nth-child(4){background:linear-gradient(160deg,#3f3a37 0%,#8e7a60 45%,#d8c8a4 100%)}
.card .cap{position:absolute;left:0;bottom:0;width:100%;height:64px;background:var(--green);color:#fff;text-align:center;font-size:10px;font-weight:700;line-height:14px;padding-top:12px}
.card .cap b{display:block;font-weight:400;font-size:10px;margin-top:1px}

/* testimonial */
.say{left:0;top:2400px;width:1200px;height:314px;background:var(--soft)}
.say-title{left:242px;top:2434px}
.quote-mark{left:242px;top:2508px}
.say-text{left:341px;top:2502px;width:262px;font-size:10px;line-height:14px;font-style:italic;color:var(--text)}
.say-name{left:341px;top:2578px;font-size:10.5px;font-weight:700;color:#2d3137}
.dots{left:341px;top:2620px;display:flex;gap:6px}
.dots i{width:6px;height:6px;border-radius:50%;background:#c4c9cf;display:block}
.dots i:first-child{background:var(--blue)}
.person{left:786px;top:2431px;width:176px;height:283px;background:linear-gradient(180deg,#e9ecf0 0%,#b7c8dc 45%,#8aa3c0 100%);border-radius:80px 80px 0 0}

/* footer */
.footer{left:0;top:2714px;width:1200px;height:342px;background:var(--footer);color:#d2d6dc}
.footer .logo{left:242px;top:69px;height:37px;font-size:22px;padding:0 8px;border-width:2px}
.f-about{left:242px;top:124px;width:168px;font-size:9.5px;line-height:14.5px}
.footer .social{left:242px;top:252px}
.f-col{position:absolute;top:83px}
.f-col h4{font-size:10.5px;font-weight:700;color:#fff;letter-spacing:.3px;margin-bottom:22px}
.contact-row{display:flex;gap:12px;font-size:9.5px;line-height:14px;margin-bottom:16px}
.contact-row svg{flex:none;margin-top:1px}
.f-list{list-style:none;font-size:9.5px;line-height:22px}
.f-list li{display:flex;gap:12px;align-items:center}
.f-list li.cont{padding-left:18px}
.bottombar{left:0;top:3056px;width:1200px;height:47px;background:var(--footer-deep);color:#8e949c;font-size:8.5px}
.bottombar .copy{position:absolute;left:242px;top:17px}
.bottombar .legal{position:absolute;right:242px;top:17px;color:#fff}
</style>
</head>
<body>
<div class="page">

  <div class="abs topbar">
    <span class="call">Call Us: +12 555 0147</span>
    <span class="follow">Follow Us:</span>
    <div class="social"><span></span><span></span><span></span></div>
  </div>

  <header class="abs header">
    <div class="logo">bramwelloq</div>
    <a class="abs btn-signin" href="#">
      <svg width="12" height="12" viewBox="0 0 12 12"><rect x="6" y="1" width="5" height="10" fill="none" stroke="#fff" stroke-width="1.4"/><path d="M1 6h6M5 3.5L7.5 6 5 8.5" fill="none" stroke="#fff" stroke-width="1.4"/></svg>SIGNIN
    </a>
    <a class="abs btn-register" href="#">
      <svg width="12" height="12" viewBox="0 0 12 12"><path d="M2 10l1-3 6-6 2 2-6 6z" fill="#fff"/></svg>REGISTER
    </a>
  </header>

  <nav class="abs nav">
    <ul><li>ABOUT</li><li>RISK WARNING</li><li>FAQS</li><li>TRADING GLOSSARY</li><li>CONTACT</li></ul>
  </nav>

  <section class="abs hero" role="img" aria-label="Photo of a trader watching market screens">
    <h1>LOREM IPSUM DOLOR<br>SIT AMET</h1>
    <p>Lorem ipsum dolor sit amet, consectetur adipisicing elit, sed do eiusmod tempor incididunt ut labore et dolore magna aliqua. Ut enim ad minim veniam,</p>
    <div class="split-btn" style="left:242px;top:316px;width:170px;height:50px">
      <span class="label" style="width:130px">LEARN MORE</span>
      <span class="go"><svg width="9" height="14" viewBox="0 0 9 14"><path d="M1 1l6 6-6 6" fill="none" stroke="#1565c8" stroke-width="1.6"/></svg></span>
    </div>
    <div class="slide-arrow" style="left:0"><svg width="9" height="14" viewBox="0 0 9 14"><path d="M8 1L2 7l6 6" fill="none" stroke="#fff" stroke-width="2"/></svg></div>
    <div class="slide-arrow" style="right:0"><svg width="9" height="14" viewBox="0 0 9 14"><path d="M1 1l6 6-6 6" fill="none" stroke="#fff" stroke-width="2"/></svg></div>
  </section>

  <div class="feature" style="left:242px">
    <svg width="34" height="46" viewBox="0 0 34 46"><path d="M10 26l-4 18 8-4 3 5 3-17z M24 26l4 18-8-4-3 5-3-17z" fill="#1565c8"/><circle cx="17" cy="16" r="14" fill="#1565c8"/><circle cx="17" cy="16" r="9" fill="#fff"/><circle cx="17" cy="16" r="6" fill="#1565c8"/></svg>
    <div><h3>THE BEST IN TOWN</h3><p>Lorem ipsum dolor sit amet, consectetur adipisicing elit, sed do eiusmod tempor incididunt ut labore et dolore magna aliqua.</p></div>
  </div>
  <div class="feature" style="left:488px">
    <svg width="38" height="40" viewBox="0 0 38 40"><circle cx="19" cy="9" r="7" fill="#1565c8"/><path d="M8 30c0-8 5-13 11-13s11 5 11 13z" fill="#1565c8"/><circle cx="6" cy="20" r="4.5" fill="#1565c8"/><circle cx="32" cy="20" r="4.5" fill="#1565c8"/><path d="M0 36c0-5 3-8 6-8s6 3 6 8zM26 36c0-5 3-8 6-8s6 3 6 8z" fill="#1565c8"/></svg>
    <div><h3>BEST PROFESSIONAL AGENTS</h3><p>Lorem ipsum dolor sit amet, consectetur adipisicing elit, sed do eiusmod tempor incididunt ut labore et dolore magna aliqua.</p></div>
  </div>
  <div class="feature" style="left:730px">
    <svg width="40" height="34" viewBox="0 0 40 34"><path d="M8 2h24l7 9-19 21L1 11z" fill="#1565c8"/><path d="M1 11h38M14 2l-3 9 9 21 9-21-3-9" fill="none" stroke="#fff" stroke-width="1.5"/></svg>
    <div><h3>BEST SUPPORT</h3><p>Lorem ipsum dolor sit amet, consectetur adipisicing elit, sed do eiusmod tempor incididunt ut labore et dolore magna aliqua.</p></div>
  </div>
  <div class="abs divider"></div>

  <h2 class="abs section-title why-title">Why Join Us?</h2>
  <p class="abs why-text">Lorem ipsum dolor sit amet, consectetur adipisicing elit, sed do eiusmod tempor incididunt ut labore et dolore magna aliqua. Ut enim ad minim veniam.</p>
  <ul class="abs ticks">
    <li><svg width="26" height="22" viewBox="0 0 26 22"><path d="M2 12l7 7L24 2" fill="none" stroke="#1565c8" stroke-width="3"/><path d="M1 21h14" stroke="#1565c8" stroke-width="2"/></svg>Best trading tips ever</li>
    <li><svg width="26" height="22" viewBox="0 0 26 22"><path d="M2 12l7 7L24 2" fill="none" stroke="#1565c8" stroke-width="3"/><path d="M1 21h14" stroke="#1565c8" stroke-width="2"/></svg>Secret tips from Experts</li>
    <li><svg width="26" height="22" viewBox="0 0 26 22"><path d="M2 12l7 7L24 2" fill="none" stroke="#1565c8" stroke-width="3"/><path d="M1 21h14" stroke="#1565c8" stroke-width="2"/></svg>We teach you how to trade online</li>
    <li><svg width="26" height="22" viewBox="0 0 26 22"><path d="M2 12l7 7L24 2" fill="none" stroke="#1565c8" stroke-width="3"/><path d="M1 21h14" stroke="#1565c8" stroke-width="2"/></svg>Learn how to trade Commodities</li>
    <li><svg width="26" height="22" viewBox="0 0 26 22"><path d="M2 12l7 7L24 2" fill="none" stroke="#1565c8" stroke-width="3"/><path d="M1 21h14" stroke="#1565c8" stroke-width="2"/></svg>Learn how to become a Trader</li>
  </ul>
  <div class="split-btn" style="left:242px;top:1320px;width:170px;height:50px">
    <span class="label" style="width:130px">REGISTER</span>
    <span class="go"><svg width="9" height="14" viewBox="0 0 9 14"><path d="M1 1l6 6-6 6" fill="none" stroke="#1565c8" stroke-width="1.6"/></svg></span>
  </div>
  <div class="abs why-photo" role="img" aria-label="Photo of business people reviewing charts on a table"></div>

  <section class="abs join" role="img" aria-label="Photo of a financial newspaper with coins">
    <h2>JOIN OUR<br>SCHOOL NOW!</h2>
    <p>Lorem ipsum dolor sit amet, consectetur adipisicing elit, sed do eiusmod tempor incididunt ut labore et dolore magna aliqua.</p>
    <div class="field" style="top:58px">First Name</div>
    <div class="field" style="top:101px">Last Name</div>
    <div class="field" style="top:145px">Email</div>
    <div class="agree"><i></i>I agree to terms and conditions.</div>
    <div class="split-btn" style="left:730px;top:217px;width:104px;height:30px">
      <span class="label" style="width:80px;padding-left:26px;font-size:10px">SEND</span>
      <span class="go"><svg width="6" height="10" viewBox="0 0 6 10"><path d="M1 1l4 4-4 4" fill="none" stroke="#1565c8" stroke-width="1.4"/></svg></span>
    </div>
  </section>

  <h2 class="abs section-title offer-title">What do we Offer!</h2>
  <p class="abs offer-text">Lorem ipsum dolor sit amet, consectetur adipisicing elit, sed do eiusmod tempor incididunt ut labore et dolore magna aliqua. Ut enim ad minim veniam, quis nostrud exercitation ullamco laboris nisi ut aliquip ex ea commodo consequat. Duis aute irure dolor in reprehenderit in voluptate velit esse cillum dolore eu fugiat nulla pariatur. Excepteur sint occaecat cupidatat non proident, sunt in</p>
  <div class="abs cards">
    <div class="card" role="img" aria-label="Photo of a hand on a calculator"><div class="cap">Lorem ipsum dolor sit<br>amet, consectetur<b>›</b></div></div>
    <div class="card" role="img" aria-label="Photo of calculator keys"><div class="cap">Lorem ipsum dolor sit<br>amet, consectetur<b>›</b></div></div>
    <div class="card" role="img" aria-label="Photo of a red calculator on documents"><div class="cap">Lorem ipsum dolor sit<br>amet, consectetur<b>›</b></div></div>
    <div class="card" role="img" aria-label="Photo of financial papers on a desk"><div class="cap">Lorem ipsum dolor sit<br>amet, consectetur<b>›</b></div></div>
  </div>

  <div class="abs say"></div>
  <h2 class="abs section-title say-title">What they say..</h2>
  <svg class="abs quote-mark" width="58" height="42" viewBox="0 0 58 42"><path d="M0 0h24v24L14 42H4l8-18H0zM32 0h24v24L46 42H36l8-18H32z" fill="#17a633"/></svg>
  <p class="abs say-text">Lorem ipsum dolor sit amet, consectetur adipisicing elit, sed do eiusmod tempor incididunt ut labore et dolore magna aliqua. Ut enim ad minim veniam, quis nostrud exercitation ullamco !</p>
  <div class="abs say-name">John Doe</div>
  <div class="abs dots"><i></i><i></i><i></i></div>
  <div class="abs person" role="img" aria-label="Photo of a smiling man in a blue shirt with arms crossed"></div>

  <footer class="abs footer">
    <div class="logo">bramwelloq</div>
    <p class="abs f-about">Lorem ipsum dolor sit amet, consectetur adipisicing elit, sed do eiusmod tempor incididunt ut labore et dolore magna aliqua. Ut enim ad minim veniam, quis nostrud exercitation ullamco laboris nisi ut aliquip ex ea commodo consequat.</p>
    <div class="social"><span></span><span></span><span></span></div>

    <div class="f-col" style="left:426px">
      <h4>CONTACT INFO</h4>
      <div class="contact-row"><svg width="11" height="14" viewBox="0 0 11 14"><path d="M5.5 14S0 8 0 5.5a5.5 5.5 0 0111 0C11 8 5.5 14 5.5 14z" fill="#1565c8"/><circle cx="5.5" cy="5.5" r="2" fill="#232a35"/></svg><span>14 Harlow Lane<br>Westbridge<br>40517<br>Norland</span></div>
      <div class="contact-row"><svg width="12" height="10" viewBox="0 0 12 10"><rect width="12" height="10" fill="#1565c8"/><path d="M0 0l6 5 6-5" fill="none" stroke="#232a35" stroke-width="1.2"/></svg><span>hello@bramwelloq.com</span></div>
      <div class="contact-row"><svg width="12" height="12" viewBox="0 0 12 12"><path d="M2 0l3 3-1.5 2A7 7 0 007 8.5L9 7l3 3-2 2C5 12 0 7 0 2z" fill="#1565c8"/></svg><span>(0480) 555-019283</span></div>
    </div>

    <div class="f-col" style="left:608px">
      <h4>OUR SERVICES</h4>
      <ul class="f-list">
        <li><svg width="6" height="9" viewBox="0 0 6 9"><path d="M1 1l3.5 3.5L1 8" fill="none" stroke="#1565c8" stroke-width="1.4"/></svg>Lorem ipsum dolor sit</li>
        <li class="cont">amet, consectetur</li>
        <li><svg width="6" height="9" viewBox="0 0 6 9"><path d="M1 1l3.5 3.5L1 8" fill="none" stroke="#1565c8" stroke-width="1.4"/></svg>adipisicing elit, sed do</li>
        <li class="cont">eiusmod tempor</li>
        <li><svg width="6" height="9" viewBox="0 0 6 9"><path d="M1 1l3.5 3.5L1 8" fill="none" stroke="#1565c8" stroke-width="1.4"/></svg>incididunt ut labore et</li>
        <li class="cont">dolore magna aliqua. Ut</li>
        <li><svg width="6" height="9" viewBox="0 0 6 9"><path d="M1 1l3.5 3.5L1 8" fill="none" stroke="#1565c8" stroke-width="1.4"/></svg>enim ad minim veniam,</li>
        <li class="cont">quis nostrud</li>
      </ul>
    </div>

    <div class="f-col" style="left:792px">
      <h4>ADDITIONAL LINKS</h4>
      <ul class="f-list">
        <li><svg width="6" height="9" viewBox="0 0 6 9"><path d="M1 1l3.5 3.5L1 8" fill="none" stroke="#1565c8" stroke-width="1.4"/></svg>Lorem ipsum dolor sit</li>
        <li class="cont">amet, consectetur</li>
        <li><svg width="6" height="9" viewBox="0 0 6 9"><path d="M1 1l3.5 3.5L1 8" fill="none" stroke="#1565c8" stroke-width="1.4"/></svg>adipisicing elit, sed do</li>
        <li class="cont">eiusmod tempor</li>
      </ul>
    </div>
  </footer>

  <div class="abs bottombar">
    <span class="copy">© Copyright Bramwelloq 2016. All Rights Reserved.</span>
    <span class="legal">Terms &amp; Conditions &nbsp;&nbsp;/&nbsp;&nbsp; Privacy Protection</span>
  </div>

</div>
</body>
</html>
```